Business Cards

The name of our firm is "Tallpine Insurance adjusters"
We separate ourselves from all other public adjusters because most of us worked for the insurance companies so we understand their games.
As Insurance adjusters we represent the Insured, not the insurance companies. Our # 1 priority is to handle the entire claim process as seamless as possible on behalf of the homeowner/business owner so they don't have to deal with the hassles and headaches. Just as the logo your team designed, I want the cards to stand out from everyone elses. I also want the cards to help better understand our services and Value on hiring us and value that we can offer.
I uploaded the logo whenever I created the project. I don't see an option on re uploading the logo anywhere. Any advise??

```html
<!DOCTYPE html>
<html lang="en">
<head>
<meta charset="utf-8">
<title>Tallpine Insurance Adjusters – Business Cards</title>
<link href="https://fonts.googleapis.com/css2?family=Open+Sans:wght@400;700;800&display=swap" rel="stylesheet">
<style>
  :root {
    --bg: #e9ebee;
    --blue-deep: #0b4a78;
    --blue: #13679c;
    --blue-light: #1f7fb6;
    --ink-dark: #3a3b3d;
    --white: #ffffff;
    --mark-on-blue: #083d63;
  }
  * { margin: 0; padding: 0; box-sizing: border-box; }
  html, body {
    width: 1200px; height: 900px; overflow: hidden;
    background: var(--bg);
    font-family: "Open Sans", Arial, sans-serif;
  }
  .sheet { position: relative; width: 1200px; height: 900px; }
  .card {
    position: absolute; left: 290px; width: 620px; height: 354px;
    border-radius: 22px; overflow: hidden;
    box-shadow: 0 6px 18px rgba(0,0,0,0.18);
  }
  .card--back {
    top: 80px;
    background: linear-gradient(135deg, var(--blue-deep) 0%, var(--blue) 60%, var(--blue-light) 100%);
  }
  .card--front { top: 494px; background: var(--white); }
  .card__wave { position: absolute; inset: 0; width: 620px; height: 354px; }

  .brand {
    position: absolute; display: flex; align-items: center; gap: 12px;
    font-weight: 800; text-transform: uppercase;
  }
  .brand__square { width: 18px; height: 18px; background: currentColor; flex: none; }
  .brand__text { display: flex; flex-direction: column; line-height: 1.05; }
  .brand__name { font-size: 34px; letter-spacing: 1px; }
  .brand__tag { font-size: 12.5px; letter-spacing: 2.4px; }

  .card--back .brand {
    left: 50%; top: 50%; transform: translate(-50%, -50%);
    color: var(--mark-on-blue);
  }
  .card--back .brand__name { font-size: 48px; }
  .card--back .brand__tag { font-size: 17px; letter-spacing: 3.6px; }
  .card--back .brand__square { width: 26px; height: 26px; }

  .card--front .brand { left: 372px; top: 118px; color: var(--blue); }

  .person { position: absolute; left: 38px; top: 158px; color: var(--white); }
  .person__name { font-size: 26px; font-weight: 700; letter-spacing: 1.5px; text-transform: uppercase; line-height: 1.1; white-space: nowrap; }
  .person__title { font-size: 17px; font-weight: 400; margin-top: 2px; }
  .contact { list-style: none; margin-top: 14px; }
  .contact__item { display: flex; align-items: center; gap: 10px; font-size: 16px; line-height: 1.6; }
  .contact__icon { width: 15px; height: 15px; fill: var(--white); flex: none; }
</style>
</head>
<body>
<main class="sheet">

  <section class="card card--back" aria-label="Card back">
    <div class="brand">
      <span class="brand__square"></span>
      <span class="brand__text">
        <span class="brand__name">Tallpine</span>
        <span class="brand__tag">Insurance Adjusters</span>
      </span>
    </div>
  </section>

  <section class="card card--front" aria-label="Card front">
    <svg class="card__wave" viewBox="0 0 620 354" aria-hidden="true">
      <defs>
        <linearGradient id="waveFill" x1="0" y1="0" x2="1" y2="1">
          <stop offset="0" stop-color="#0b4a78"/>
          <stop offset="1" stop-color="#1a74ab"/>
        </linearGradient>
      </defs>
      <path d="M0,110 C200,80 340,110 410,230 C465,320 540,318 620,300 L620,354 L0,354 Z" fill="url(#waveFill)"/>
      <path d="M0,110 C200,80 340,110 410,230 C465,320 540,318 620,300" fill="none" stroke="#ffffff" stroke-width="8"/>
      <path d="M30,95 C215,70 350,104 422,224 C478,312 545,310 600,296" fill="none" stroke="#3a3b3d" stroke-width="5"/>
    </svg>

    <div class="person">
      <h1 class="person__name">Daniel Marrow</h1>
      <p class="person__title">Founder/CEO</p>
      <ul class="contact">
        <li class="contact__item">
          <svg class="contact__icon" viewBox="0 0 24 24" aria-hidden="true"><path d="M6.6 10.8a15.1 15.1 0 0 0 6.6 6.6l2.2-2.2a1 1 0 0 1 1-.25 11.4 11.4 0 0 0 3.6.57 1 1 0 0 1 1 1V20a1 1 0 0 1-1 1A17 17 0 0 1 3 4a1 1 0 0 1 1-1h3.5a1 1 0 0 1 1 1c0 1.25.2 2.45.57 3.6a1 1 0 0 1-.25 1z"/></svg>
          555-014-7720
        </li>
        <li class="contact__item">
          <svg class="contact__icon" viewBox="0 0 24 24" aria-hidden="true"><path d="M2 5h20v14H2z M4 7v.4l8 5.2 8-5.2V7z" fill-rule="evenodd"/></svg>
          daniel@tallpineinsadj.com
        </li>
        <li class="contact__item">
          <svg class="contact__icon" viewBox="0 0 24 24" aria-hidden="true"><path d="M12 2a10 10 0 1 0 0 20 10 10 0 0 0 0-20zm-1 17.9A8 8 0 0 1 4.1 11H8c.1 3 1.2 6.4 3 8.9zM8 9H4.1A8 8 0 0 1 11 4.1C9.2 6.6 8.1 6 8 9zm5 10.9c1.8-2.5 2.9-5.9 3-8.9h3.9a8 8 0 0 1-6.9 8.9zM16 9c-.1-3-1.2-2.4-3-4.9A8 8 0 0 1 19.9 9z"/></svg>
          www.tallpineinsadj.com
        </li>
      </ul>
    </div>

    <div class="brand">
      <span class="brand__square"></span>
      <span class="brand__text">
        <span class="brand__name">Tallpine</span>
        <span class="brand__tag">Insurance Adjusters</span>
      </span>
    </div>
  </section>

</main>
</body>
</html>
```